Women's Shelter Website Design

We are working with a Women's Shelter in California. They provide services and shelter for women and mothers throughout California.
Some sites to use for inspiration:
https://harborlightcommons.org
https://qbrtl.org
https://www.kemjy.org
https://plmfarrowby.org
https://www.gvhollow.org (I love the banner, navigation and upper navigation)
https://bellmereroost.org (love the idea of an EXIT NOW button)
Thank you for taking the time to consider designing a website for us. We are web developers based in Stockton, CA, USA. Most of our projects go through the same process. Understanding this process may help you win a project with us. We custom-code all of our websites in-house. We don’t have any requirements as to what tools you use for your design, but we ask that you follow these guidelines.
IMAGES:
If you use any images or icons in the design, we ask that you have a link to the asset so we can purchase the image/icon. Most of the designs we submit do not have the customer’s images on them unless they have some great images. Be creative; show us the feeling you are trying to portray with your image choices. Use any royalty-free site you choose. We subscribe to Adobe and mainly use their images, but we can purchase images outside of Adobe. PLEASE NOTE: we will not submit designs to clients with watermarks on the images.
FONTS:
We ask that you identify the fonts you’re using in the design. This can be done in a message if you want. We typically use Google Fonts and Adobe Fonts.
CONTENT:
We're always open to different content and ideas. We often submit designs with stock images so the client can see our vision. We typically take pictures after the website launch to use their images with our vision. Lorem Ipsum is fine for paragraphs, but we ask that you make the Headers with correct English. We want to be able to show the vision and identify the sections of the website.
INSPIRATION:
We typically add a couple of links in the brief of websites we like to help you get started in your design.
REVISIONS:
We do not often ask for revisions of the designs unless we see something in the design that may not appeal to the client. If there are slight changes that we want to make, we do that in the development process.
FEEDBACK:
We rarely give feedback on designs during the design process. We are working on many website projects and do not have the time to provide feedback. We usually respond if your request is well thought out and asks specific questions, but a note asking “feedback, please” usually goes unanswered.

```html
<!DOCTYPE html>
<html lang="en">
<head>
<meta charset="utf-8">
<title>Lumen Grove Womens Shelter</title>
<link href="https://fonts.googleapis.com/css2?family=Poppins:ital,wght@0,400;0,500;0,600;0,700;1,400&display=swap" rel="stylesheet">
<style>
:root{
  --purple:#5a3296;
  --purple-dark:#4a2782;
  --purple-soft:#b9a6d6;
  --coral:#f97b5c;
  --red:#e8191f;
  --ink:#1d1d1d;
  --muted:#555;
  --pale:#f7f5fa;
  --white:#fff;
}
*{box-sizing:border-box;margin:0;padding:0}
html,body{width:1200px;height:4518px;overflow:hidden}
body{font-family:'Poppins',sans-serif;color:var(--ink);background:var(--white)}
.page{position:relative;width:1200px;height:4518px;overflow:hidden}
.abs{position:absolute}
.btn{position:absolute;display:flex;align-items:center;justify-content:center;border-radius:40px;font-weight:500;color:var(--white);background:var(--purple)}
.ph{position:absolute}
.section-title{position:absolute;left:0;width:1200px;text-align:center;font-weight:600;font-size:50px}
.section-lead{position:absolute;left:0;width:1200px;text-align:center;font-size:15px;line-height:26px;color:var(--muted)}
.arrow{position:absolute;width:48px;height:60px;background:var(--coral);display:flex;align-items:center;justify-content:center}
/* header */
.brand{position:absolute;left:88px;top:66px;display:flex;align-items:center;gap:10px}
.brand-dot{width:26px;height:26px;border-radius:50%;background:var(--purple)}
.brand-name{font-weight:600;font-size:30px;color:var(--ink)}
.hotline-icon{position:absolute;left:652px;top:32px;width:52px;height:52px;border-radius:8px;background:var(--coral);display:flex;align-items:center;justify-content:center}
.hotline-title{position:absolute;left:714px;top:26px;font-weight:600;font-size:26px;color:var(--purple)}
.hotline-num{position:absolute;left:714px;top:58px;font-size:20px;color:#333}
.nav{position:absolute;top:104px;left:485px;display:flex;gap:28px;font-size:15px;color:#333}
/* hero */
.hero{position:absolute;left:0;top:149px;width:1200px;height:646px;background:linear-gradient(90deg,#c9b392 0%,#d5c3a3 45%,#d9c9ab 100%)}
.hero-title{position:absolute;left:560px;top:336px;width:600px;text-align:center;font-weight:700;font-size:50px;line-height:62px}
/* mission */
.mission-text{position:absolute;left:624px;top:1058px;width:440px;font-size:15px;line-height:31px;color:var(--muted);text-align:justify}
.bullets{position:absolute;left:666px;top:1186px;list-style:none;font-size:15px;color:#333}
.bullets li{height:37px;display:flex;align-items:center;gap:20px}
.bullets li::before{content:"";width:10px;height:10px;border-radius:50%;background:var(--purple)}
/* services */
.service-card{position:absolute;top:1824px;width:322px;height:380px}
.service-bar{position:absolute;left:0;top:0;width:322px;height:7px;background:var(--coral)}
.service-img{position:absolute;left:0;top:7px;width:322px;height:378px}
.service-body{position:absolute;left:38px;top:278px;width:284px;height:250px;background:var(--pale);padding:36px 28px 0 28px}
.service-body h3{font-weight:500;font-size:20px;margin-bottom:18px}
.service-body p{font-size:14.5px;line-height:26px;color:var(--muted);text-align:justify}
.service-body .btn{position:static;width:138px;height:40px;font-size:13px;margin-top:38px}
/* involved */
.inv-card{position:absolute;top:2822px;width:316px;height:380px}
.inv-cap{position:absolute;left:0;bottom:0;width:100%;height:96px;background:rgba(90,50,150,.85);color:var(--white);font-weight:600;font-size:22px;display:flex;align-items:center;justify-content:center}
.inv-mid{background:var(--purple);color:var(--white);text-align:center}
.inv-mid h3{font-weight:600;font-size:22px;margin-top:64px}
.inv-mid hr{width:36px;border:0;border-top:2px solid var(--coral);margin:16px auto 18px}
.inv-mid p{font-size:15px;line-height:31px;padding:0 36px}
/* events */
.event-card{position:absolute;top:3650px;width:316px;height:300px}
.event-img{position:absolute;left:0;top:0;width:316px;height:200px}
.event-body{position:absolute;left:0;top:109px;width:254px;height:188px;background:var(--white);padding:32px 34px 0 34px}
.event-date{font-size:11px;color:#444}
.event-body h3{font-weight:600;font-size:20px;margin:8px 0 8px}
.event-body p{font-size:12px;line-height:19px;color:#333}
.event-body a{display:block;margin-top:16px;font-size:13px;font-style:italic;color:var(--purple);text-decoration:underline}
/* footer */
.footer{position:absolute;left:0;top:4092px;width:1200px;height:367px;background:var(--purple);color:var(--white)}
.footer h4{position:absolute;font-weight:600;font-size:20px;text-decoration:underline;text-decoration-color:var(--coral);text-underline-offset:6px}
.flinks{position:absolute;left:398px;top:160px;list-style:none;font-size:15px}
.flinks li{height:31px;display:flex;align-items:center;gap:14px}
.flinks li::before{content:"";width:8px;height:8px;border-radius:50%;background:var(--coral)}
.contact{position:absolute;left:579px;font-size:14.5px;line-height:18px;display:flex;gap:20px;align-items:flex-start}
.cicon{width:32px;height:32px;border:1px solid rgba(255,255,255,.6);border-radius:5px;display:flex;align-items:center;justify-content:center;flex:none}
.social{position:absolute;top:4368px;width:30px;height:30px;border:1.5px solid var(--coral);border-radius:3px;display:flex;align-items:center;justify-content:center}
.social span{width:14px;height:14px;background:var(--coral);border-radius:2px}
.copy{position:absolute;left:0;top:4459px;width:1200px;height:59px;background:var(--coral);color:var(--white);font-size:13px;display:flex;align-items:center;justify-content:center}
</style>
</head>
<body>
<div class="page">

  <header>
    <div class="brand"><span class="brand-dot"></span><span class="brand-name">Lumen Grove</span></div>
    <div class="hotline-icon">
      <svg width="28" height="28" viewBox="0 0 24 24" fill="none" stroke="#5a3296" stroke-width="2"><path d="M5 3h4l2 5-3 2a12 12 0 0 0 6 6l2-3 5 2v4a2 2 0 0 1-2 2A18 18 0 0 1 3 5a2 2 0 0 1 2-2z"/></svg>
    </div>
    <div class="hotline-title">24-Hour Hotline</div>
    <div class="hotline-num">8015 552 0147</div>
    <div class="btn" style="left:973px;top:32px;width:141px;height:47px;font-size:15px">DONATE</div>
    <nav class="nav"><span>Home</span><span>About Us</span><span>Services</span><span>Get Involved</span><span>Get Help</span><span>Blog</span><span>Contact Us</span></nav>
  </header>

  <section class="hero" role="img" aria-label="Photo of a smiling mother hugging her young daughter who holds a bouquet of pink tulips"></section>
  <h1 class="hero-title abs">Welcome to Lumen Grove Womens Shelter</h1>
  <div class="btn" style="left:742px;top:503px;width:226px;height:90px;font-size:24px">DONATE</div>
  <div class="btn" style="left:942px;top:759px;width:189px;height:74px;font-size:24px;background:var(--red);gap:14px">
    <svg width="20" height="20" viewBox="0 0 20 20" stroke="#fff" stroke-width="3.5"><path d="M3 3l14 14M17 3L3 17"/></svg>Exit Now
  </div>

  <div class="ph" style="left:112px;top:1145px;width:306px;height:285px;background:var(--purple-soft)" role="img" aria-label="Decorative dotted texture in purple"></div>
  <div class="abs" style="left:140px;top:975px;width:362px;height:423px;border:2px solid var(--coral)"></div>
  <div class="ph" style="left:168px;top:951px;width:358px;height:421px;background:linear-gradient(135deg,#7d9bb0,#c9b8a8 55%,#e9e4de)" role="img" aria-label="Photo of a mother kissing her baby"></div>
  <h2 class="abs" style="left:623px;top:962px;font-weight:600;font-size:42px">Our Mission</h2>
  <p class="mission-text">Lorem ipsum dolor sit amet, consectetur adipiscing elit, sed do eiusmod tempor incididunt ut labore et dolore magna aliqua. Ut enim ad minim veniam, quis nostrud</p>
  <ul class="bullets">
    <li>Lorem ipsum dolor sit amet, consectetur</li>
    <li>Lorem ipsum dolor sit amet, consectetur</li>
    <li>Lorem ipsum dolor sit amet, consectetur</li>
  </ul>
  <div class="btn" style="left:626px;top:1351px;width:165px;height:58px;font-size:14px">READ MORE</div>

  <div class="abs" style="left:0;top:1526px;width:1200px;height:398px;background:var(--purple)"></div>
  <div class="abs" style="left:0;top:1924px;width:1200px;height:597px;background:var(--pale)"></div>
  <h2 class="section-title" style="top:1630px;color:var(--white)">Services</h2>
  <p class="section-lead" style="top:1720px;color:var(--white)">Lorem ipsum dolor sit amet, consectetur adipiscing elit. Maecenas ornare<br>nulla ut dui euismod pretium. Sed varius sagittis lacus, a tincidunt dui</p>

  <div class="service-card" style="left:84px">
    <div class="service-bar"></div>
    <div class="service-img ph" role="img" aria-label="Photo of a mother hugging her daughter" style="background:linear-gradient(135deg,#e8e4df,#bdb4ab)"></div>
    <div class="service-body"><h3>Service 1</h3><p>Lorem ipsum dolor sit amet, consecte tur adipiscing elit. euismod pretium</p><div class="btn">READ MORE</div></div>
  </div>
  <div class="service-card" style="left:440px">
    <div class="service-bar"></div>
    <div class="service-img ph" role="img" aria-label="Photo of a mother and daughter sharing a drink" style="background:linear-gradient(135deg,#f1ede6,#d8c4b0)"></div>
    <div class="service-body"><h3>Service 2</h3><p>Lorem ipsum dolor sit amet, consecte tur adipiscing elit. euismod pretium</p><div class="btn">READ MORE</div></div>
  </div>
  <div class="service-card" style="left:795px">
    <div class="service-bar"></div>
    <div class="service-img ph" role="img" aria-label="Photo of a daughter kissing her mother outdoors" style="background:linear-gradient(135deg,#6f7d5c,#c9534b 60%,#e4d9cf)"></div>
    <div class="service-body"><h3>Service 3</h3><p>Lorem ipsum dolor sit amet, consecte tur adipiscing elit. euismod pretium</p><div class="btn">READ MORE</div></div>
  </div>
  <div class="arrow" style="left:998px;top:2422px"><svg width="12" height="14" viewBox="0 0 12 14" stroke="#fff" stroke-width="1.5" fill="none"><path d="M8 2L3 7l5 5"/></svg></div>
  <div class="arrow" style="left:1065px;top:2422px"><svg width="12" height="14" viewBox="0 0 12 14" stroke="#fff" stroke-width="1.5" fill="none"><path d="M4 2l5 5-5 5"/></svg></div>

  <h2 class="section-title" style="top:2610px">Get Involved</h2>
  <p class="section-lead" style="top:2709px">Lorem ipsum dolor sit amet, consectetur adipiscing elit. Maecenas ornare<br>nulla ut dui euismod pretium. Sed varius sagittis lacus, a tincidunt dui</p>
  <div class="abs" style="left:0;top:2885px;width:1200px;height:246px;background:var(--coral)"></div>
  <div class="inv-card ph" style="left:84px;background:linear-gradient(180deg,#c8d6e6,#6c7a6a 60%,#3c4a3c)" role="img" aria-label="Photo of volunteers distributing boxes of supplies">
    <div class="inv-cap">Lorem ipsum dolor sit</div>
  </div>
  <div class="inv-card inv-mid" style="left:444px">
    <h3>Lorem ipsum dolor</h3><hr>
    <p>Lorem ipsum dolor sit amet, consectetur adipiscing elit. Maecenas vel mattis magna. Cras purus sem, facilisis non</p>
    <div class="btn" style="left:75px;top:270px;width:166px;height:57px;font-size:16px;background:var(--coral)">DONATE NOW</div>
  </div>
  <div class="inv-card ph" style="left:802px;background:linear-gradient(160deg,#5c4a44,#a08a78 55%,#3a2e2c)" role="img" aria-label="Photo of many hands stacked together">
    <div class="inv-cap">Lorem ipsum dolor sit</div>
  </div>
  <div class="arrow" style="left:998px;top:3250px"><svg width="12" height="14" viewBox="0 0 12 14" stroke="#fff" stroke-width="1.5" fill="none"><path d="M8 2L3 7l5 5"/></svg></div>
  <div class="arrow" style="left:1065px;top:3250px"><svg width="12" height="14" viewBox="0 0 12 14" stroke="#fff" stroke-width="1.5" fill="none"><path d="M4 2l5 5-5 5"/></svg></div>

  <div class="abs" style="left:0;top:3382px;width:1200px;height:710px;background:var(--pale)"></div>
  <h2 class="section-title" style="top:3468px">Upcoming Events</h2>
  <p class="section-lead" style="top:3551px">Lorem ipsum dolor sit amet, consectetur adipiscing elit. Maecenas ornare<br>nulla ut dui euismod pretium. Sed varius sagittis lacus, a tincidunt dui</p>
  <div class="event-card" style="left:88px">
    <div class="event-img ph" role="img" aria-label="Photo of a mother and daughter at home" style="background:linear-gradient(135deg,#8a7a6c,#e4ddd3)"></div>
    <div class="event-body"><div class="event-date">JAN 25, 2023</div><h3>Post 1 Headline</h3><p>Lorem ipsum dolor sit amet, consectetur adipi</p><a>Read More</a></div>
  </div>
  <div class="event-card" style="left:444px">
    <div class="event-img ph" role="img" aria-label="Photo of a mother embracing her daughter" style="background:linear-gradient(135deg,#d8d2ca,#6b4a3a)"></div>
    <div class="event-body"><div class="event-date">JAN 25, 2023</div><h3>Post 2 Headline</h3><p>Lorem ipsum dolor sit amet, consectetur adipi</p><a>Read More</a></div>
  </div>
  <div class="event-card" style="left:798px">
    <div class="event-img ph" role="img" aria-label="Photo of a mother and children in a café" style="background:linear-gradient(135deg,#3e5a4e,#b6a89a 60%,#7a3a34)"></div>
    <div class="event-body"><div class="event-date">JAN 25, 2023</div><h3>Post 3 Headline</h3><p>Lorem ipsum dolor sit amet, consectetur adipi</p><a>Read More</a></div>
  </div>
  <div class="arrow" style="left:998px;top:3985px"><svg width="12" height="14" viewBox="0 0 12 14" stroke="#fff" stroke-width="1.5" fill="none"><path d="M8 2L3 7l5 5"/></svg></div>
  <div class="arrow" style="left:1065px;top:3985px"><svg width="12" height="14" viewBox="0 0 12 14" stroke="#fff" stroke-width="1.5" fill="none"><path d="M4 2l5 5-5 5"/></svg></div>

  <footer class="footer">
    <div class="abs" style="left:112px;top:164px;display:flex;align-items:center;gap:10px">
      <span style="width:26px;height:26px;border-radius:50%;background:var(--white)"></span>
      <span style="font-weight:600;font-size:30px">Lumen Grove</span>
    </div>
    <h4 style="left:395px;top:78px">Quick Links</h4>
    <ul class="flinks"><li>About Us</li><li>Services</li><li>Get Involved</li><li>Blog</li><li>Contact Us</li></ul>
    <h4 style="left:579px;top:78px">Contact Us</h4>
    <div class="contact" style="top:164px">
      <span class="cicon"><svg width="16" height="16" viewBox="0 0 24 24" fill="none" stroke="#f97b5c" stroke-width="2"><path d="M5 3h4l2 5-3 2a12 12 0 0 0 6 6l2-3 5 2v4a2 2 0 0 1-2 2A18 18 0 0 1 3 5a2 2 0 0 1 2-2z"/></svg></span>
      <span>CALL US<br>8015 552 0147</span>
    </div>
    <div class="contact" style="top:222px">
      <span class="cicon"><svg width="16" height="16" viewBox="0 0 24 24" fill="none" stroke="#f97b5c" stroke-width="2"><rect x="3" y="5" width="18" height="14"/><path d="M3 6l9 7 9-7"/></svg></span>
      <span>EMAIL US<br>hello@lumengrove.org</span>
    </div>
    <div class="contact" style="top:280px">
      <span class="cicon"><svg width="16" height="16" viewBox="0 0 24 24" fill="none" stroke="#f97b5c" stroke-width="2"><path d="M12 22s7-7 7-12a7 7 0 0 0-14 0c0 5 7 12 7 12z"/><circle cx="12" cy="10" r="2.5"/></svg></span>
      <span>Address line Dummy Here<br>Address line Here</span>
    </div>
    <h4 style="left:863px;top:76px">Our Newsletter</h4>
    <p class="abs" style="left:863px;top:166px;width:260px;font-size:14.5px;line-height:21px">Subscribe our newsletter to get the latest news.</p>
    <div class="abs" style="left:863px;top:223px;width:251px;height:37px;background:var(--white)"></div>
    <div class="abs" style="left:863px;top:274px;width:126px;height:33px;background:var(--coral);font-size:12px;display:flex;align-items:center;justify-content:center">SUBSCRIBE</div>
  </footer>
  <div class="social" style="left:131px"><span></span></div>
  <div class="social" style="left:170px"><span></span></div>
  <div class="social" style="left:209px"><span></span></div>
  <div class="social" style="left:256px"><span></span></div>
  <div class="copy">Copyright © 2023 All Rights Reserved By Company name</div>

</div>
</body>
</html>
```